Clean bold and classy business card front and back
Rin can be the logo
My name Dorian Hesketh as owner
Phone email and address
Owner Dorian Hesketh
Phone 8505550147
Email ridgelineinsulate@mailbox.test
Address170 frank pais rd Havana fl 32390

Industry/Entity Type

Business

Contact Information for Business Card

Owner Dorian Hesketh
Phone 8505550147

Requirements
Must have
• Ridgeline insulate co under Rin logo
Nice to have
• Bold and clean. Maybe use Rin as logo and name under it. Have logo on one side and info on the other side with logo also
• Put a pic up. It doesn't have to be that but something that can be used
• Try some fancy fonts also

```html
<!DOCTYPE html>
<html lang="en">
<head>
<meta charset="utf-8">
<title>Ridgeline Insulate Co – Business Card</title>
<link rel="stylesheet" href="https://fonts.googleapis.com/css2?family=Open+Sans:wght@400;600;700&display=swap">
<style>
  :root {
    --backdrop: #e9ebee;
    --card-white: #ffffff;
    --brand-blue: #1f86cf;
    --brand-blue-light: #2ea3e3;
    --brand-blue-deep: #0a4f9c;
    --ink: #2b2b2b;
    --ink-soft: #555b63;
    --rule: #1f86cf;
  }
  * { box-sizing: border-box; margin: 0; padding: 0; }
  html, body {
    width: 1200px; height: 913px; overflow: hidden;
    background: var(--backdrop);
    font-family: "Open Sans", Arial, sans-serif;
  }
  .sheet {
    position: relative; width: 1200px; height: 913px;
    display: flex; align-items: center; justify-content: center; gap: 50px;
  }
  .card {
    position: relative; width: 525px; height: 300px;
    border-radius: 16px; overflow: hidden;
    box-shadow: 0 10px 30px rgba(0,0,0,.18);
  }

  /* Front: contact side */
  .card--front { background: var(--card-white); }
  .front__tab {
    position: absolute; right: 0; top: 38px;
    width: 26px; height: 26px;
    background: var(--brand-blue-light);
    border-left: 5px solid #333;
  }
  .front__person {
    position: absolute; right: 36px; top: 40px; text-align: right;
  }
  .front__name {
    font-size: 25px; font-weight: 700; color: var(--brand-blue); letter-spacing: .2px;
  }
  .front__role { font-size: 12px; color: var(--ink); margin-top: -2px; }
  .front__name-rule {
    position: absolute; right: 26px; top: 96px;
    width: 250px; height: 2px; background: var(--rule);
  }
  .brand {
    position: absolute; left: 34px; top: 108px;
    color: var(--brand-blue); font-weight: 700; line-height: 1;
  }
  .brand__mark { display: flex; align-items: center; gap: 10px; }
  .brand__square { width: 18px; height: 18px; background: currentColor; }
  .brand__initials { font-size: 50px; letter-spacing: 3px; }
  .brand__name { font-size: 15px; letter-spacing: 2.5px; margin-top: 8px; text-transform: uppercase; }

  .front__contact-rule {
    position: absolute; left: 250px; top: 188px;
    width: 250px; height: 1.5px; background: var(--rule);
  }
  .contact {
    position: absolute; left: 250px; top: 200px;
    list-style: none; font-size: 13.5px; color: var(--brand-blue);
  }
  .contact__item { display: flex; align-items: center; gap: 8px; height: 22px; }
  .contact__icon { width: 12px; height: 12px; fill: #333; flex: none; }

  /* Back: logo side */
  .card--back {
    background: linear-gradient(160deg, var(--brand-blue-light) 0%, var(--brand-blue) 45%, var(--brand-blue-deep) 100%);
  }
  .card--back .brand {
    left: 0; right: 0; top: 88px; text-align: center; color: #ffffff;
  }
  .card--back .brand__mark { justify-content: center; }
  .card--back .brand__initials { font-size: 72px; }
  .card--back .brand__square { width: 24px; height: 24px; }
  .card--back .brand__name { font-size: 21px; margin-top: 12px; letter-spacing: 3.5px; }
</style>
</head>
<body>
<main class="sheet">

  <section class="card card--front" aria-label="Business card front">
    <div class="front__tab"></div>
    <div class="front__person">
      <p class="front__name">Dorian Hesketh</p>
      <p class="front__role">Owner</p>
    </div>
    <div class="front__name-rule"></div>

    <div class="brand">
      <div class="brand__mark">
        <span class="brand__initials">RIN</span>
        <span class="brand__square"></span>
      </div>
      <p class="brand__name">Ridgeline Insulate Co</p>
    </div>

    <div class="front__contact-rule"></div>
    <ul class="contact">
      <li class="contact__item">
        <svg class="contact__icon" viewBox="0 0 24 24" aria-hidden="true"><path d="M6.6 10.8a15.1 15.1 0 0 0 6.6 6.6l2.2-2.2a1 1 0 0 1 1-.25 11.4 11.4 0 0 0 3.6.57 1 1 0 0 1 1 1V20a1 1 0 0 1-1 1A17 17 0 0 1 3 4a1 1 0 0 1 1-1h3.5a1 1 0 0 1 1 1c0 1.25.2 2.45.57 3.6a1 1 0 0 1-.25 1z"/></svg>
        850 555-0147
      </li>
      <li class="contact__item">
        <svg class="contact__icon" viewBox="0 0 24 24" aria-hidden="true"><path d="M2 5h20v14H2zm2 2v.5l8 5 8-5V7zm0 2.9V17h16V9.9l-8 5z"/></svg>
        ridgelineinsulate@mailbox.test
      </li>
      <li class="contact__item">
        <svg class="contact__icon" viewBox="0 0 24 24" aria-hidden="true"><path d="M12 2a7 7 0 0 0-7 7c0 5.2 7 13 7 13s7-7.8 7-13a7 7 0 0 0-7-7zm0 9.5A2.5 2.5 0 1 1 12 6.5a2.5 2.5 0 0 1 0 5z"/></svg>
        482 tilden oak rd Havana fl 32390
      </li>
    </ul>
  </section>

  <section class="card card--back" aria-label="Business card back">
    <div class="brand">
      <div class="brand__mark">
        <span class="brand__initials">RIN</span>
        <span class="brand__square"></span>
      </div>
      <p class="brand__name">Ridgeline Insulate Co</p>
    </div>
  </section>

</main>
</body>
</html>
```